Chiropractic healthcare group business card

We are a Portland Oregon based chiropractic healthcare group. Looking for a new business card design. Something cutting edge, that shows off our new logo and tag line.Use either of the attached logos.Our tag line = "Who would you be without pain?"I'm open to about anything, impress me!!
Target Market(s)
Chiropractic patients - Auto injury, back pain, sports injuries, neck , shoulder, hip, knee, ankle pain.
Industry/Entity Type
Chiropractic
Contact Information for Business Card
Dr. Bram Tovelund, D.C.
Clinic name - Cedar Chiropractic
2 clinics
location #1
20418 NW Harlow Road
Suite B
North Plains, OR 97133
Location #2
13529 SE Marston Street
Portland OR 97236
Main phone line 971.386.4217
website : www.BirchValeCare.com
Tag line "Who would you be without pain?"
Colors
Designer to choose colors to be used in the design.
Requirements
Must have
- Use the logo colors -- Want the orange color to be a TRUE orange.
- Both clinic address
- phone number
- website
- personal email - b.tovelund@FreshStrideHealth.com
- tag line - "Who would you be without pain?"

```html
<!DOCTYPE html>
<html lang="en">
<head>
<meta charset="utf-8">
<title>Cedar Chiropractic – Business Card</title>
<link rel="stylesheet" href="https://fonts.googleapis.com/css2?family=Roboto:ital,wght@0,400;0,500;0,700;1,400&family=Saira+Semi+Condensed:wght@700&display=swap">
<style>
  :root {
    --backdrop: #3b3b3d;
    --card: #222224;
    --orange: #f7941d;
    --grey: #8d8e90;
    --white: #f2f2f2;
    --muted: #cfcfcf;
  }
  * { box-sizing: border-box; margin: 0; padding: 0; }
  html, body { width: 799px; height: 1200px; overflow: hidden; }
  body {
    background: var(--backdrop);
    font-family: "Roboto", Arial, sans-serif;
    color: var(--white);
    position: relative;
  }
  .card {
    position: absolute;
    left: 60px;
    width: 680px;
    height: 390px;
    background: var(--card);
    border-radius: 4px;
    overflow: hidden;
    box-shadow: 0 10px 30px rgba(0,0,0,.45);
  }
  .card--front { top: 95px; }
  .card--back { top: 715px; }

  .brand {
    display: flex;
    align-items: center;
    gap: 12px;
  }
  .brand__square {
    width: 22px; height: 22px;
    background: var(--orange);
  }
  .brand__name {
    font-family: "Roboto", Arial, sans-serif;
    font-weight: 500;
    color: var(--grey);
    text-transform: uppercase;
    letter-spacing: 6px;
  }
  .card--front .brand {
    position: absolute;
    left: 0; right: 0; top: 120px;
    justify-content: center;
  }
  .card--front .brand__name { font-size: 34px; }

  .clinics {
    position: absolute;
    left: 40px; top: 250px;
    list-style: none;
    font-size: 16.5px;
    line-height: 30px;
  }
  .clinics__label { color: var(--orange); text-transform: uppercase; }

  .card--back .brand { position: absolute; left: 36px; top: 34px; }
  .card--back .brand__square { width: 18px; height: 18px; }
  .card--back .brand__name { font-size: 22px; letter-spacing: 4px; }

  .tagline {
    position: absolute; left: 36px; top: 72px;
    color: var(--orange);
    font-style: italic;
    font-size: 15px;
  }
  .person { position: absolute; left: 36px; top: 118px; }
  .person__name {
    font-family: "Saira Semi Condensed", "Roboto", sans-serif;
    font-weight: 700;
    color: var(--orange);
    font-size: 22px;
    line-height: 26px;
  }
  .person__title { font-size: 15px; color: var(--muted); margin-top: 2px; }

  .contacts {
    position: absolute; left: 36px; top: 200px;
    list-style: none;
    font-size: 15.5px;
    line-height: 30px;
  }
  .contacts li { display: flex; align-items: center; gap: 14px; }
  .contacts svg { width: 14px; height: 14px; flex: none; }

  .corner-mark {
    position: absolute;
    right: -70px; bottom: -70px;
    width: 300px; height: 300px;
    background: var(--orange);
  }
</style>
</head>
<body>
  <section class="card card--front">
    <div class="brand">
      <span class="brand__square"></span>
      <span class="brand__name">Cedar Chiropractic</span>
    </div>
    <ul class="clinics">
      <li><span class="clinics__label">Our Clinic#1:</span> 20418 NW Harlow Road Suite B North Plains, OR 97133</li>
      <li><span class="clinics__label">Our Clinic#2:</span> 13529 SE Marston Street Portland OR 97236</li>
    </ul>
  </section>

  <section class="card card--back">
    <div class="brand">
      <span class="brand__square"></span>
      <span class="brand__name">Cedar Chiropractic</span>
    </div>
    <p class="tagline">Who would you be without pain?</p>
    <div class="person">
      <p class="person__name">Dr. Bram Tovelund, D.C.</p>
      <p class="person__title">Chiropractic Doctor</p>
    </div>
    <ul class="contacts">
      <li>
        <svg viewBox="0 0 16 16" aria-hidden="true"><path fill="#f7941d" d="M3.6 1.5l2.3 2.6-1.2 1.8c.9 2 2.4 3.5 4.4 4.4l1.8-1.2 2.6 2.3-1.3 2.1C7 13.3 2.7 9 1.5 3.8z"/></svg>
        971.386.4217
      </li>
      <li>
        <svg viewBox="0 0 16 16" aria-hidden="true"><rect x="1" y="3" width="14" height="10" fill="#f7941d"/><path d="M1.5 3.5L8 9l6.5-5.5" stroke="#222224" stroke-width="1.3" fill="none"/></svg>
        www.BirchValeCare.com
      </li>
      <li>
        <svg viewBox="0 0 16 16" aria-hidden="true"><circle cx="8" cy="8" r="6.5" fill="none" stroke="#f7941d" stroke-width="1.5"/><ellipse cx="8" cy="8" rx="2.8" ry="6.5" fill="none" stroke="#f7941d" stroke-width="1.2"/><path d="M1.5 8h13" stroke="#f7941d" stroke-width="1.2"/></svg>
        b.tovelund@FreshStrideHealth.com
      </li>
    </ul>
    <div class="corner-mark" aria-hidden="true"></div>
  </section>
</body>
</html>
```